Banner Ad to promote Youth Cycling Camps

We need a 728 x 90 banner ad to promote some youth cycling camps. There are 2 different camps - a road camp where they learn to ride their bikes on the roads and a mountain bike camp. The camps teach bike handling skills and racing tactics.

Target Market(s)

Parents of youth ages 7-17

Industry/Entity Type

Non-Profit

Font styles to use
Sans Serif

Requirements
Must have
• Logo
• Dates - Road Camp May 5-7, 2017
• - Mountain Bike Camp July 14-16, 2017
• website - pedalwaycircuit.org
• be 728 x 90
Nice to have
• Animated - would like it to rotate with 3 slides - 1 a focus on both camps, 1 on road camp, 1 on mountain bike camp

```html
<!DOCTYPE html>
<html lang="en">
<head>
<meta charset="utf-8">
<title>Pedalway Circuit – Youth Cycling Camp Banners</title>
<link rel="stylesheet" href="https://fonts.googleapis.com/css2?family=Bebas+Neue&family=Open+Sans:ital,wght@1,700&display=swap">
<style>
  :root {
    --canvas: #efefef;
    --sky: #6ec6ea;
    --leaf: #8dc63f;
    --sun: #f5e625;
    --panel: rgba(0, 0, 0, 0.55);
    --band: rgba(232, 232, 232, 0.86);
    --ink: #1d1d1d;
    --forest-a: #2f3a2c;
    --forest-b: #6d6450;
    --road-a: #3d3b3a;
    --road-b: #8a8a8c;
  }
  * { margin: 0; padding: 0; box-sizing: border-box; }
  html, body {
    width: 1200px; height: 590px; overflow: hidden;
    background: var(--canvas);
  }
  .banner {
    position: absolute; left: 238px; width: 728px; height: 90px;
    overflow: hidden;
    box-shadow: 0 9px 14px rgba(0, 0, 0, 0.38);
  }
  .banner--both { top: 100px; }
  .banner--split { top: 250px; }
  .banner--road { top: 400px; }

  .photo { position: absolute; top: 0; height: 90px; }
  .photo--mountain {
    background: linear-gradient(180deg, var(--forest-a) 0%, #3e4a36 45%, var(--forest-b) 100%);
  }
  .photo--road {
    background: linear-gradient(100deg, #5a2a26 0%, var(--road-a) 35%, var(--road-b) 100%);
  }

  .camp-panel {
    position: absolute; top: 6px; width: 310px; height: 51px;
    background: var(--panel); border-radius: 6px;
  }
  .camp-title {
    position: absolute; top: 6px;
    font-family: "Bebas Neue", sans-serif; font-size: 26.5px; line-height: 1;
    letter-spacing: 2px; white-space: nowrap;
  }
  .camp-title--mountain { color: var(--sky); }
  .camp-title--road { color: var(--leaf); }
  .camp-dates {
    position: absolute; top: 30px;
    font-family: "Open Sans", sans-serif; font-style: italic; font-weight: 700;
    font-size: 14.5px; line-height: 1; color: var(--sun); white-space: nowrap;
  }
  .camp-panel--right { left: 418px; }
  .camp-panel--right .camp-title,
  .camp-panel--right .camp-dates { left: 20px; }
  .camp-panel--left { left: 0; }
  .camp-panel--left .camp-title,
  .camp-panel--left .camp-dates { right: 20px; text-align: right; }

  .url-band {
    position: absolute; left: 0; top: 64px; width: 728px; height: 18px;
    background: var(--band);
    font-family: "Bebas Neue", sans-serif; font-size: 14px; line-height: 19px;
    letter-spacing: 2.6px; color: var(--ink); text-align: center;
    padding-left: 4px;
  }

  .brand {
    position: absolute; top: 8px; width: 76px;
    display: flex; flex-direction: column; align-items: center; gap: 3px;
  }
  .brand-dot {
    width: 14px; height: 14px; border-radius: 50%; background: var(--sky);
  }
  .brand-name {
    font-family: "Bebas Neue", sans-serif; font-size: 18px; line-height: 18px;
    letter-spacing: 1px; color: var(--sky); text-align: center;
  }
</style>
</head>
<body>

<section class="banner banner--both">
  <div class="photo photo--mountain" style="left:0;width:728px" role="img" aria-label="Group of young riders on a forest trail"></div>
  <div class="brand" style="left:37px">
    <span class="brand-dot"></span><span class="brand-name">Pedalway<br>Circuit</span>
  </div>
  <div class="camp-panel camp-panel--right">
    <p class="camp-title camp-title--mountain">Mountain Bike Camp</p>
    <p class="camp-dates">Friday to Sunday,&nbsp; July 14-16, 2017</p>
  </div>
  <p class="url-band">http://pedalwaycircuit.org/</p>
</section>

<section class="banner banner--split">
  <div class="photo photo--road" style="left:0;width:364px" role="img" aria-label="Young riders cornering on a road course"></div>
  <div class="photo photo--mountain" style="left:364px;width:364px" role="img" aria-label="Riders heading up a forest trail"></div>
  <div class="camp-panel camp-panel--left">
    <p class="camp-title camp-title--road">Road Bike Camp</p>
    <p class="camp-dates">Friday to Sunday, May 5,6,7, 2017</p>
  </div>
  <div class="camp-panel camp-panel--right">
    <p class="camp-title camp-title--mountain">Mountain Bike Camp</p>
    <p class="camp-dates">Friday to Sunday,&nbsp; July 14-16, 2017</p>
  </div>
  <p class="url-band">http://pedalwaycircuit.org/</p>
  <div class="brand" style="left:326px">
    <span class="brand-dot"></span><span class="brand-name">Pedalway<br>Circuit</span>
  </div>
</section>

<section class="banner banner--road">
  <div class="photo photo--road" style="left:0;width:728px" role="img" aria-label="Young road cyclists riding past cones in a parking lot"></div>
  <div class="camp-panel camp-panel--left">
    <p class="camp-title camp-title--road">Road Camp</p>
    <p class="camp-dates">Friday to Sunday, May 5,6,7, 2017</p>
  </div>
  <p class="url-band">http://pedalwaycircuit.org/</p>
  <div class="brand" style="left:614px">
    <span class="brand-dot"></span><span class="brand-name">Pedalway<br>Circuit</span>
  </div>
</section>

</body>
</html>
```